KAZ Freightworks #ALLKAZ Business Cards & Letterhead

I am looking to business cards designed for our organization. We are currently undergoing a small re-branding that is taking place. Our organization is called KAZ Freightworks and we are headquartered in Phoenix, AZ. We primarily provide transportation and logistics services to the Meridel Parcel Bureau who is our largest customer. I would like to see a design that incorporates name, title, contact info, website, and address (this will be different depending on the employee). I would also like to see some color on the business card using our logo colors or a variation. I would like our logo on the back of the business card with the website displayed. The final design should communicate that we are a next generation transportation operate that focuses on being driver-first, customer-centric, innovative, and sustainable.We would also like our #ALLKAZ catch phrase incorporated as well.
Updates

Decision maker traveling outside of the country until Monday, November 25th.

Target Market(s)

Transportation & Logistics

Industry/Entity Type

Trucking Company

Contact Information for Business Card

-First and Last Name
-Position Title
-Contact Phone
-Contact Email
-Physical Address

Font styles to use
Serif

Colors

Designer to choose colors to be used in the design.

Requirements
Must have
• -KAZ logo prominently displayed
• -#ALLKAZ catch phrase used
• -Some amount of color, design gradient, etc.
• -Logo on the back with website listed (https://www.kazfreightco.example)

```html
<!DOCTYPE html>
<html lang="en">
<head>
<meta charset="utf-8">
<title>KAZ Freightworks Business Card</title>
<link href="https://fonts.googleapis.com/css2?family=Josefin+Sans:wght@700&family=Pathway+Gothic+One&display=swap" rel="stylesheet">
<style>
  :root {
    --bg: #e4e2de;
    --card-pale: #ebebec;
    --card-grey: #c9cacc;
    --brand-green: #6cc04a;
    --brand-ink: #0f3440;
  }
  html, body {
    margin: 0;
    width: 1200px;
    height: 800px;
    overflow: hidden;
    background: var(--bg);
  }
  .sheet {
    position: relative;
    width: 1200px;
    height: 800px;
    display: flex;
    align-items: center;
    justify-content: center;
    gap: 24px;
  }
  .card {
    width: 560px;
    height: 336px;
    display: block;
    box-shadow: 0 10px 24px rgba(0,0,0,0.22);
  }
  .display { font-family: "Josefin Sans", sans-serif; font-weight: 700; fill: var(--brand-ink); }
  .body-text { font-family: "Pathway Gothic One", sans-serif; fill: var(--brand-ink); }
</style>
</head>
<body>
<main class="sheet">

  <!-- Card front: website and brand name -->
  <svg class="card card-front" viewBox="0 0 882 529" role="group" aria-label="Card front">
    <defs>
      <filter id="panel-shadow" x="-20%" y="-20%" width="140%" height="140%">
        <feDropShadow dx="4" dy="0" stdDeviation="8" flood-color="#000" flood-opacity="0.28"/>
      </filter>
    </defs>
    <rect class="panel-grey" width="882" height="529" fill="var(--card-grey)"/>
    <polygon class="accent-green" points="160,0 383,0 283,117" fill="var(--brand-green)"/>
    <polygon class="accent-green" points="150,529 375,529 272,410" fill="var(--brand-green)"/>
    <polygon class="panel-pale" points="0,0 160,0 418,262 150,529 0,529" fill="var(--card-pale)" filter="url(#panel-shadow)"/>
    <text class="body-text website" x="70" y="277" font-size="38">www.kazfreightco.example</text>

    <g class="brand-name">
      <text class="display" x="623" y="300" font-size="118" text-anchor="middle">KAZ</text>
      <text class="display tagline" x="623" y="372" font-size="42" text-anchor="middle">#ALLKAZ</text>
    </g>
  </svg>

  <!-- Card back: contact details -->
  <svg class="card card-back" viewBox="0 0 882 529" role="group" aria-label="Card back">
    <defs>
      <filter id="panel-shadow-back" x="-20%" y="-20%" width="140%" height="140%">
        <feDropShadow dx="-4" dy="0" stdDeviation="8" flood-color="#000" flood-opacity="0.28"/>
      </filter>
    </defs>
    <rect class="panel-grey" width="882" height="529" fill="var(--card-grey)"/>
    <polygon class="accent-green" points="497,0 717,0 597,120" fill="var(--brand-green)"/>
    <polygon class="accent-green" points="497,529 727,529 602,400" fill="var(--brand-green)"/>
    <line class="accent-ink" x1="472" y1="0" x2="597" y2="125" stroke="var(--brand-ink)" stroke-width="13"/>
    <line class="accent-ink" x1="482" y1="529" x2="602" y2="405" stroke="var(--brand-ink)" stroke-width="13"/>
    <polygon class="panel-pale" points="717,0 882,0 882,529 727,529 459,262" fill="var(--card-pale)" filter="url(#panel-shadow-back)"/>

    <g class="brand-name">
      <text class="display" x="675" y="290" font-size="88" text-anchor="middle">KAZ</text>
      <text class="display tagline" x="675" y="343" font-size="31" text-anchor="middle">#ALLKAZ</text>
    </g>

    <g class="contact">
      <text class="display name" x="90" y="128" font-size="40">ROSA MERLAND</text>
      <text class="display title" x="90" y="152" font-size="18" letter-spacing="5">CHAIRMAN &amp; CEO</text>

      <path class="icon-phone" d="M94 198 q-4 4 -2 12 q4 14 16 22 q7 4 11 0 l3 -3 -8 -7 -4 3 q-7 -4 -10 -12 l3 -4 -6 -8z" fill="var(--brand-ink)"/>
      <text class="body-text phone" x="122" y="227" font-size="46">555-014-0392</text>

      <path class="icon-pin" d="M101 273 a9 9 0 0 1 9 9 c0 7 -9 15 -9 15 s-9 -8 -9 -15 a9 9 0 0 1 9 -9z M101 279 a3 3 0 1 0 0.01 0z M91 301 h20" fill="var(--brand-ink)" stroke="var(--brand-ink)" stroke-width="1.5"/>
      <text class="body-text address" font-size="27">
        <tspan x="122" y="300">Corporate Office - Tempe, AZ</tspan>
        <tspan x="122" y="329">KAZ Freightworks &amp; Energy Services, Inc.</tspan>
        <tspan x="122" y="358">4120 North Canyon Ridge Road</tspan>
        <tspan x="122" y="388">Tempe, AZ 85281</tspan>
      </text>

      <g class="icon-globe" fill="none" stroke="var(--brand-ink)" stroke-width="2.2">
        <circle cx="102" cy="433" r="10"/>
        <ellipse cx="102" cy="433" rx="4.5" ry="10"/>
        <line x1="92" y1="433" x2="112" y2="433"/>
      </g>
      <text class="body-text email" x="122" y="444" font-size="32">info@kazfreightco.example</text>
    </g>
  </svg>

</main>
</body>
</html>
```